Business Card Design - Crisp & Clean

Looking for a new clean and crisp business card design. Design must incorporate our corporate colors (see attached style sheet). We're a pretty fun loving group who likes to keep it light while still portraying a professional image. Card should incorporate both our logo and our mascot (see attachment). Card should be double sided and should have room for our social media - Facebook, Linked In and Twitter on the back. Font selections do not have to match the style guide.

```html
<!DOCTYPE html>
<html lang="en">
<head>
<meta charset="utf-8">
<title>KeenHR Business Card</title>
<link href="https://fonts.googleapis.com/css2?family=Roboto:wght@400;700;900&display=swap" rel="stylesheet">
<style>
  :root {
    --backdrop: #72675a;
    --paper: #ffffff;
    --brand-yellow: #fdcf08;
    --brand-yellow-soft: #fedc3a;
    --ink: #111111;
    --text-grey: #5b5b5b;
    --social-blue: #3b8fd0;
  }
  * { margin: 0; padding: 0; box-sizing: border-box; }
  html, body { width: 1200px; height: 1000px; overflow: hidden; }
  body {
    background: var(--backdrop);
    font-family: "Roboto", Arial, sans-serif;
    position: relative;
  }
  .card {
    position: absolute;
    left: 231px;
    width: 707px;
    height: 432px;
    background: var(--paper);
  }
  .card--front { top: 46px; }
  .card--back { top: 534px; }

  .front-panel {
    position: absolute;
    left: 16px; top: 16px;
    width: 675px; height: 400px;
    background: var(--brand-yellow);
    overflow: hidden;
  }
  .front-decoration {
    position: absolute;
    left: 440px; top: 0;
    width: 240px; height: 400px;
    background: radial-gradient(ellipse at 60% 55%, var(--brand-yellow-soft) 0%, rgba(254,220,58,0.4) 45%, rgba(253,207,8,0) 72%);
  }

  .brand {
    position: absolute;
    display: flex;
    align-items: center;
    gap: 14px;
  }
  .brand__mark {
    width: 40px; height: 40px;
    border-radius: 50%;
  }
  .brand__words { display: flex; flex-direction: column; }
  .brand__name {
    font-weight: 900;
    font-size: 38px;
    line-height: 1;
    letter-spacing: 0.5px;
  }
  .brand__tagline {
    font-weight: 700;
    font-size: 8.5px;
    letter-spacing: 0.2px;
    margin-top: 4px;
    text-transform: uppercase;
  }

  .brand--front { left: 198px; top: 178px; color: var(--paper); }
  .brand--front .brand__mark { background: var(--paper); }

  .brand--back { left: 58px; top: 191px; color: var(--ink); }
  .brand--back .brand__mark { background: var(--brand-yellow); }

  .divider {
    position: absolute;
    left: 373px; top: 79px;
    width: 3px; height: 274px;
    background: var(--brand-yellow);
  }
  .contact {
    position: absolute;
    left: 406px; top: 82px;
    color: var(--text-grey);
  }
  .contact__name { font-size: 21px; font-weight: 400; line-height: 26px; }
  .contact__role { font-size: 15px; color: var(--brand-yellow); line-height: 20px; }
  .contact__details { margin-top: 44px; font-size: 18px; line-height: 23px; }

  .social {
    position: absolute;
    left: 406px; top: 306px;
    display: flex;
    gap: 18px;
  }
  .social__icon { width: 30px; height: 30px; }
  .social__icon--one { background: #3b5998; }
  .social__icon--two { background: var(--social-blue); border-radius: 50%; }
  .social__icon--three { background: #1a77b5; }

  .mascot {
    position: absolute;
    left: 600px; top: 66px;
    width: 96px; height: 190px;
    border-radius: 40px 40px 10px 10px;
    background: linear-gradient(180deg, #e8e8e8 0%, #f3eee6 40%, #5a4a3e 80%, rgba(255,255,255,0) 100%);
  }
</style>
</head>
<body>
  <section class="card card--front">
    <div class="front-panel">
      <div class="front-decoration" role="img" aria-label="Large faint brand symbol decoration"></div>
      <div class="brand brand--front">
        <span class="brand__mark"></span>
        <div class="brand__words">
          <span class="brand__name">KeenHR</span>
          <span class="brand__tagline">HR Process Management Solutions</span>
        </div>
      </div>
    </div>
  </section>

  <section class="card card--back">
    <div class="brand brand--back">
      <span class="brand__mark"></span>
      <div class="brand__words">
        <span class="brand__name">KeenHR</span>
        <span class="brand__tagline">HR Process Management Solutions</span>
      </div>
    </div>

    <div class="divider"></div>

    <div class="contact">
      <p class="contact__name">Maren Holt</p>
      <p class="contact__role">Marketing Wizard</p>
      <div class="contact__details">
        <p>maren@keenhr.com</p>
        <p>Mobile: 555-013-2468</p>
      </div>
    </div>

    <div class="social" aria-label="Social media links">
      <span class="social__icon social__icon--one"></span>
      <span class="social__icon social__icon--two"></span>
      <span class="social__icon social__icon--three"></span>
    </div>

    <div class="mascot" role="img" aria-label="Company mascot: cartoon scientist pointing toward the contact details"></div>
  </section>
</body>
</html>
```